UI design for Media player size 800x480

We need to create mobile media UI 800x480 in size (In addition, please use the grey scale in colors for now)

We are designing our own media app ui for in car use similar to drivelink (http://www.pomerix.com/dash/drivelink/?cid=wwa-us-kwg-features-com) or velto ride (http://www.gadgetvoxa.com/velto-ride)

I am providing the exact specs as well as the layout. Please keep in mind that the layout and sizes much follow ours. All we are looking for is the creativity in design. We would like the design look sleek - simple yet sophisticated and elegant, with the modern spice in it.

Target Market(s)

consumers

Industry/Entity Type

Automotive

Font styles to use
Sans Serif

Requirements
Must have
• exact layout as provided in the attachement and the size of 800x480
Should not have
• please do not change the layout.

```html
<!DOCTYPE html>
<html lang="en">
<head>
<meta charset="utf-8">
<title>Media Player – Artists</title>
<link rel="stylesheet" href="https://fonts.googleapis.com/css2?family=Roboto:wght@400;500;700&display=swap">
<style>
  :root{
    --rail-light:#c9c9c9;
    --rail-dark:#7d7d7d;
    --nav-bg:#1d1d1d;
    --list-bg:#3b3b3b;
    --divider:#555555;
    --text:#ffffff;
    --text-muted:#bdbdbd;
    --text-dim:#9a9a9a;
    --accent:#f4c430;
    --header-blue:#2aa8df;
    --header-light:#4fc0ec;
    --pill-blue:#1d8fc9;
    --pill-dark:#161616;
    --selected-top:#f4f4f4;
    --selected-bottom:#c6c6c6;
    --selected-text:#7a7a7a;
  }
  *{box-sizing:border-box;margin:0;padding:0}
  html,body{width:1200px;height:720px;overflow:hidden;background:#000}
  body{font-family:'Roboto',sans-serif;color:var(--text)}
  .screen{position:relative;width:1200px;height:720px;overflow:hidden;background:var(--list-bg)}

  /* left rail */
  .rail{position:absolute;left:0;top:0;width:90px;height:720px;
    background:repeating-linear-gradient(0deg,rgba(255,255,255,.06) 0 2px,rgba(0,0,0,.05) 2px 4px),
      linear-gradient(90deg,var(--rail-dark),var(--rail-light) 55%,var(--rail-dark))}
  .src-badge{position:absolute;left:12px;top:36px;width:63px;height:36px;border-radius:7px;
    background:var(--accent);color:#5a4300;font-weight:500;font-size:20px;
    display:flex;align-items:center;justify-content:center}
  .clock{position:absolute;left:0;top:108px;width:90px;text-align:center;font-weight:700;
    font-size:20px;line-height:23px}

  /* navigation */
  .nav{position:absolute;left:90px;top:0;width:308px;height:720px;background:var(--nav-bg)}
  .source{position:absolute;top:38px;left:0;width:100%;text-align:center;color:var(--accent);
    font-weight:700;font-size:21px}
  .nav-item{position:absolute;left:0;width:308px;height:74px;display:flex;align-items:center;
    font-weight:500;font-size:22px;letter-spacing:.3px}
  .nav-item svg{position:absolute;left:60px;width:34px;height:34px}
  .nav-item span{position:absolute;left:114px}
  .nav-item.is-selected{background:linear-gradient(var(--selected-top),var(--selected-bottom));color:var(--selected-text)}

  .mic{position:absolute;left:-16px;top:612px;width:136px;height:136px;border-radius:50%;
    background:#fff;box-shadow:0 0 8px rgba(0,0,0,.4)}
  .mic svg{position:absolute;left:40px;top:30px}

  /* header */
  .header{position:absolute;left:398px;top:0;width:802px;height:97px;overflow:hidden;
    background:linear-gradient(120deg,var(--header-light),var(--header-blue) 60%)}
  .header .shard{position:absolute;top:0;left:0}
  .back{position:absolute;left:50px;top:34px}
  .header-title{position:absolute;left:107px;top:36px;font-weight:500;font-size:23px;letter-spacing:.5px}
  .now-playing{position:absolute;left:379px;top:17px;width:402px;height:63px;border-radius:32px;
    background:var(--pill-blue)}
  .cover{position:absolute;left:3px;top:0;width:66px;height:63px;
    background:linear-gradient(135deg,#c9a267,#6b4a2c)}
  .cover-play{position:absolute;left:24px;top:18px}
  .track-artist{position:absolute;left:84px;top:5px;color:var(--accent);font-weight:700;font-size:22px}
  .track-title{position:absolute;left:84px;top:31px;font-size:22px;white-space:nowrap;width:300px;
    overflow:hidden;text-overflow:ellipsis}

  /* list */
  .artist-list{position:absolute;left:432px;top:97px;width:563px;list-style:none}
  .artist{height:75px;border-bottom:1.5px solid var(--divider);display:flex;align-items:center;
    justify-content:space-between;padding:0 14px}
  .artist-name{font-size:35px;font-weight:500}
  .album-count{font-size:23px;font-weight:500;color:var(--text-muted)}
  .artist.is-compact .artist-name{font-size:27px;color:var(--text-muted)}
  .artist.is-compact .album-count{color:var(--text-dim)}
  .fade{position:absolute;left:398px;top:620px;width:802px;height:100px;
    background:linear-gradient(rgba(59,59,59,0),var(--list-bg))}

  .scroll-track{position:absolute;left:1043px;top:128px;width:4px;height:538px;background:#1f1f1f}
  .scroll-thumb{position:absolute;left:1039px;top:203px;width:12px;height:104px;border-radius:6px;background:#fff}

  .alpha-jump{position:absolute;left:1086px;top:284px;width:90px;height:196px;border-radius:45px;
    background:var(--pill-dark);display:flex;flex-direction:column;align-items:center;justify-content:center;gap:8px}
  .alpha-jump span{font-weight:500;font-size:33px}
</style>
</head>
<body>
<div class="screen">
  <div class="rail">
    <div class="src-badge">SRC</div>
    <div class="clock">10:38<br>PM</div>
  </div>

  <nav class="nav">
    <div class="source">• VOXO</div>
    <div class="nav-item" style="top:97px">
      <svg viewBox="0 0 34 34" fill="none" stroke="#fff" stroke-width="2"><path d="M3 8h10l3 3h15v16H3z"/></svg><span>FOLDERS</span></div>
    <div class="nav-item" style="top:171px">
      <svg viewBox="0 0 34 34" fill="none" stroke="#fff" stroke-width="2"><path d="M9 5v20"/><circle cx="6" cy="25" r="3" fill="#fff"/><path d="M9 5l5 3M16 10h15M16 16h15M16 22h15M16 28h15"/></svg><span>PLAYLISTS</span></div>
    <div class="nav-item is-selected" style="top:247px">
      <svg viewBox="0 0 34 34" fill="none" stroke="#8a8a8a" stroke-width="2"><circle cx="17" cy="11" r="6"/><path d="M5 30c0-7 5-11 12-11s12 4 12 11z"/></svg><span>ARTISTS</span></div>
    <div class="nav-item" style="top:321px">
      <svg viewBox="0 0 34 34" fill="none" stroke="#fff" stroke-width="2"><circle cx="17" cy="17" r="13"/><circle cx="17" cy="17" r="3" fill="#fff"/><path d="M9 14a9 9 0 0 0 0 6M25 14a9 9 0 0 1 0 6"/></svg><span>ALBUMS</span></div>
    <div class="nav-item" style="top:397px">
      <svg viewBox="0 0 34 34" fill="#fff"><path d="M12 6l16-3v19h-2V9L14 11v15h-2z"/><circle cx="9" cy="26" r="4"/><circle cx="23" cy="23" r="4"/></svg><span>GENRES</span></div>
    <div class="nav-item" style="top:471px">
      <svg viewBox="0 0 34 34" fill="none" stroke="#fff" stroke-width="2.5"><circle cx="14" cy="14" r="9"/><path d="M21 21l9 9"/></svg><span>SEARCH</span></div>
  </nav>

  <div class="mic">
    <svg width="40" height="64" viewBox="0 0 40 64" fill="none" stroke="#9a9a9a" stroke-width="3"><rect x="12" y="3" width="16" height="32" rx="8"/><path d="M5 26a15 15 0 0 0 30 0M20 41v12M12 53h16"/></svg>
  </div>

  <header class="header">
    <svg class="shard" width="802" height="97" viewBox="0 0 802 97">
      <path d="M0 0h260l-140 97H0z" fill="#fff" opacity=".08"/>
      <path d="M300 0h240L360 97h-140z" fill="#fff" opacity=".06"/>
      <path d="M600 0h202v60z" fill="#fff" opacity=".07"/>
    </svg>
    <svg class="back" width="20" height="30" viewBox="0 0 20 30" fill="none" stroke="#fff" stroke-width="3.5"><path d="M15 3L4 15l11 12"/></svg>
    <div class="header-title">ARTISTS</div>
    <div class="now-playing">
      <div class="cover" role="img" aria-label="Album cover art for the current track"></div>
      <svg class="cover-play" width="26" height="28" viewBox="0 0 26 28" fill="none" stroke="#fff" stroke-width="3"><path d="M3 2l20 12L3 26z"/></svg>
      <div class="track-artist">HARLAN BRIGHTWOOD</div>
      <div class="track-title">If You Could Hear My Heart</div>
    </div>
  </header>

  <ul class="artist-list">
    <li class="artist"><span class="artist-name">Baylands</span><span class="album-count">2 Albums</span></li>
    <li class="artist"><span class="artist-name">The Barrows</span><span class="album-count">6 Albums</span></li>
    <li class="artist"><span class="artist-name">Beacon Boys</span><span class="album-count">3 Albums</span></li>
    <li class="artist"><span class="artist-name">Beacon Hall</span><span class="album-count">1 Album</span></li>
    <li class="artist"><span class="artist-name">The Belvaries</span><span class="album-count">5 Albums</span></li>
    <li class="artist"><span class="artist-name">Bexa</span><span class="album-count">2 Albums</span></li>
    <li class="artist is-compact"><span class="artist-name">Bello and Sorrentine Compilation</span><span class="album-count">4 Albums</span></li>
    <li class="artist"><span class="artist-name">Birnie</span><span class="album-count">1 Album</span></li>
  </ul>
  <div class="fade"></div>

  <div class="scroll-track"></div>
  <div class="scroll-thumb"></div>

  <div class="alpha-jump">
    <svg width="22" height="26" viewBox="0 0 22 26" fill="#fff"><path d="M11 1L1 12h7v13h6V12h7z"/></svg>
    <span>abc</span>
    <svg width="22" height="26" viewBox="0 0 22 26" fill="#fff"><path d="M11 25L1 14h7V1h6v13h7z"/></svg>
  </div>
</div>
</body>
</html>
```